Crestwell Renewal Business Card Design Phase 2

Professional and clean design. The design colors should flow with the logo. Two-sided card with the website on the back which is:

www.CrestwellRenewal.example.

"Specializing in Water Damage Restoration"

On the front I need the name, email, phone, and logo.

Name: Dorian Halvek
Email: Dorian@CrestwellRenewal.example
Phone: 555-318-2046 for now

I only have the Preview and Thumbnail right now but should have the source files uploaded within a day or two.

Target Market(s)

Flood victims, home owners with water damage from busted pipes etc...

Industry/Entity Type

Business

Contact Information for Business Card

Name: Dorian Halvek

Font styles to use
Serif
Sans Serif

Requirements
Must have
• Business Card Details Info

```html
<!DOCTYPE html>
<html lang="en">
<head>
<meta charset="utf-8">
<title>Crestwell Renewal – Business Card</title>
<link rel="stylesheet" href="https://fonts.googleapis.com/css2?family=Oswald:wght@500;700&family=Roboto:wght@400;500&display=swap">
<style>
  :root {
    --navy: #1f3d73;
    --navy-deep: #17305e;
    --navy-light: #2d5390;
    --green: #5cae4c;
    --green-light: #74c25f;
    --white: #ffffff;
    --paper: #f3f4f6;
    --stage: #e7e4de;
  }
  * { margin: 0; padding: 0; box-sizing: border-box; }
  html, body { width: 1200px; height: 1023px; overflow: hidden; }
  body {
    background: var(--stage);
    position: relative;
    font-family: "Roboto", Arial, sans-serif;
  }
  .card {
    position: absolute;
    left: 190px;
    width: 820px;
    height: 469px;
    overflow: hidden;
    box-shadow: 0 10px 28px rgba(0,0,0,0.22);
  }
  .card--front { top: 30px; background: var(--paper); }
  .card--back {
    top: 524px;
    background: radial-gradient(ellipse at 40% 30%, var(--navy-light) 0%, var(--navy) 55%, var(--navy-deep) 100%);
    color: var(--white);
  }
  .card-bands { position: absolute; inset: 0; width: 100%; height: 100%; }

  .holder {
    position: absolute;
    left: 34px;
    bottom: 58px;
    font-family: "Oswald", "Arial Narrow", sans-serif;
  }
  .holder-name {
    color: var(--green-light);
    font-weight: 700;
    font-size: 28px;
    letter-spacing: 1px;
    text-transform: uppercase;
    white-space: nowrap;
  }
  .holder-role {
    color: var(--white);
    font-family: "Roboto", Arial, sans-serif;
    font-size: 16px;
    letter-spacing: 1.5px;
    margin-top: 4px;
  }

  .brand-mark {
    position: absolute;
    top: 40px;
    left: 378px;
    width: 160px;
    font-family: "Oswald", "Arial Narrow", sans-serif;
    font-weight: 700;
    font-size: 32px;
    line-height: 1;
    letter-spacing: 1px;
    text-transform: uppercase;
    color: var(--navy);
  }

  .scene-art {
    position: absolute;
    left: 300px;
    top: 170px;
    width: 250px;
    height: 290px;
    background: linear-gradient(160deg, rgba(45,83,144,0.55) 0%, rgba(31,61,115,0.85) 100%);
    clip-path: polygon(18% 0, 88% 0, 66% 100%, 2% 100%);
  }

  .contact {
    position: absolute;
    right: 28px;
    bottom: 44px;
    text-align: right;
    color: var(--white);
    font-size: 16px;
    line-height: 1.8;
    white-space: nowrap;
  }

  .tagline {
    position: absolute;
    top: 110px;
    left: 0;
    width: 100%;
    text-align: center;
    font-family: "Oswald", "Arial Narrow", sans-serif;
    font-weight: 700;
    font-size: 17px;
    letter-spacing: 1.2px;
    text-transform: uppercase;
  }
  .back-brand {
    position: absolute;
    top: 138px;
    left: 0;
    width: 100%;
    text-align: center;
    font-family: "Oswald", "Arial Narrow", sans-serif;
    font-weight: 700;
    font-size: 84px;
    line-height: 0.95;
    letter-spacing: 2px;
    text-transform: uppercase;
    color: var(--white);
  }
  .back-site {
    position: absolute;
    bottom: 44px;
    left: 0;
    width: 100%;
    text-align: center;
    font-size: 22px;
    letter-spacing: 0.5px;
  }
  .back-site .accent { color: var(--green-light); }
</style>
</head>
<body>

<section class="card card--front" aria-label="Business card front">
  <svg class="card-bands" viewBox="0 0 820 469" preserveAspectRatio="none" aria-hidden="true">
    <polygon points="0,0 330,0 250,469 0,469" fill="var(--navy)"/>
    <polygon points="330,0 370,0 290,469 250,469" fill="var(--green)"/>
    <polygon points="560,0 580,0 490,469 470,469" fill="var(--navy)"/>
    <polygon points="580,0 820,0 820,469 490,469" fill="var(--green)"/>
  </svg>

  <div class="brand-mark">Crestwell<br>Renewal</div>

  <div class="scene-art" role="img" aria-label="Illustration of a technician spraying water beside a house"></div>

  <div class="holder">
    <div class="holder-name">Dorian Halvek</div>
    <div class="holder-role">DIRECTOR</div>
  </div>

  <div class="contact">
    <div>555-318-2046</div>
    <div>www.CrestwellRenewal.example</div>
    <div>Dorian@CrestwellRenewal.example</div>
  </div>
</section>

<section class="card card--back" aria-label="Business card back">
  <div class="tagline">Specializing in Water Damage Restoration</div>
  <div class="back-brand">Crestwell<br>Renewal</div>
  <div class="back-site">www.Crestwell<span class="accent">Renewal</span>.example</div>
</section>

</body>
</html>
```